Start up International Security Business Needs a Web Design

Based in Edinburgh UK, Varnek International Services (www.varnekis-example.com) provides security services of various types in challenging or high threat environments internationally for government and private sector organizations. We provide risk assessments, security audits and training, medical support, close protection for individuals, groups and events, crisis management, and evacuation coordination; we enable businesses to operate in challenging locations. Our experts are highly trained and qualified with exceptional experience worldwide.
The name Varnek was selected in competition and derives from Greek Mythology where it was a giant man of bronze gifted by Zeus to protect Europa from invaders and pirates, circling the island of Crete three times daily (essentially establishing a protective perimeter). The centre of the current logo (inside the "O") is a stylized symbol of Zeus; we use it as a customized "bullet" on documents and acts as an abbreviated logo.
We purposefully omitted any reference to security in the name/logo and the web-page should be discreet in the same manner - we provide services of this nature but do not draw attention to ourselves. Generic images for visuals should be used as opposed to any existing stock photography we possess as a company. Imagery that relay protection, an international reach, innovation, modern vistas, varied countrysides (desert, jungle, urban settings, an old fortress?) would be seen positively.
The current colour of blue and white in the principal logo has received positive response for the clean lines, and the grey-ish scale writing similarly works. The "O" with the symbol inside has been used as customized "bullets" inside of documents, and we envisioned several other potential uses for web pages, etc.
However the integration of bronze as a third colour given the origin of Varnek could be a consideration as well.
The final design should communicate clarity, an international reach in difficult areas with our broad experience and strength without being aggressive. There must be a section where the countries we have experience operating in is displayed graphically (i.e. a global map where the countries are coloured in). Countries are USA, Canada, UK, France, Bosnia, UAE, Qatar, Libya, Tunisia, Afghanistan, Iraq, Turkey, Sudan, Egypt, Central African Republic, Somalia, Rwanda, Somaliland. Additional sections should include "Our Clients", "Our Services", "Our Expertise", "Join Our Team" which should have a personal details form and ability to upload a CV, "Our Contact Details" which should also allow for submission of a web enquiry
Reason: Extension granted at the request of several designers in order to conceptualize solutions whilst initial selection process begins. Feedback on each design submitted will be provided. Very many thanks to all who took the time to share their vision for our company's website.
Target Market(s)
Private Sector energy, logistics, and infrastructure companies along with government organizations
Industry/Entity Type
Security
Logo Text
Varnek
Number of Pages Required
3 page
Requirements
Must have
- There must be a section where the countries we have experience operating in is displayed graphically (i.e. a global map where the countries are coloured in). Countries are USA, Canada, UK, France, Bosnia, UAE, Qatar, Libya, Tunisia, Afghanistan, Iraq, Turkey, Sudan, Egypt, Central African Republic, Somalia, Rwanda, Somaliland. Additional sections should include "Our Clients", "Our Services", "Our Expertise", "Join Our Team" which should have a personal details form and ability to upload a CV, "Our Contact Details" which should also allow for submission of a web enquiry
Should not have
- Aggressive pictures of guards, weapons, etc

```html
<!DOCTYPE html>
<html lang="en">
<head>
<meta charset="utf-8">
<title>Varnek International Services</title>
<link rel="stylesheet" href="https://fonts.googleapis.com/css2?family=Open+Sans:wght@400;600;700&family=Roboto+Condensed:wght@400;700&display=swap">
<style>
:root{
  --blue:#0a5fa8;
  --blue-dark:#084f8c;
  --sky:#5fd4f5;
  --ink:#2b2b2b;
  --grey:#555;
  --field:#ececec;
  --white:#fff;
}
*{box-sizing:border-box;margin:0;padding:0}
html,body{width:1200px;height:2711px;overflow:hidden}
body{position:relative;background:var(--white);font-family:"Open Sans",Arial,sans-serif;color:var(--ink)}
.abs{position:absolute}

/* hero */
.hero{left:0;top:0;width:1200px;height:632px;overflow:hidden}
.hero-photo{position:absolute;inset:0;background:linear-gradient(180deg,#3a3a3a 0%,#8a8682 45%,#c9c5bf 70%,#9c9893 100%)}
.brand{left:45px;top:40px;font-family:"Open Sans",Arial,sans-serif;font-weight:700;font-size:86px;color:var(--blue);line-height:1;letter-spacing:-1px}
.social{right:40px;top:44px;display:flex;gap:10px}
.social span{width:20px;height:20px;border-radius:50%;background:#3f7fc4}
.nav{right:30px;top:136px;display:flex;gap:4px;font-family:"Roboto Condensed",Arial,sans-serif;font-size:14px;font-weight:700;color:var(--white);text-transform:uppercase}
.nav a{color:inherit;text-decoration:none;padding:6px 9px}
.nav a.active{background:var(--blue);border-radius:3px}
.slider-dots{right:48px;top:480px;display:flex;gap:4px}
.slider-dots span{width:11px;height:11px;border:1px solid var(--white)}
.slider-dots span.on{background:var(--white)}
.hero-caption{left:0;top:512px;width:1200px;height:120px;background:rgba(20,20,20,.72);color:var(--white);font-weight:700;font-size:17.5px;line-height:22px;text-align:center;padding:15px 40px 0}

/* dividers */
.divider{width:52px;height:52px;border-radius:50%;background:var(--blue);border:5px solid var(--white);box-shadow:0 0 0 2px var(--blue);left:574px}

/* about */
.about-mark{left:100px;top:730px;width:240px;height:255px;border-radius:42% 42% 46% 46% / 38% 38% 50% 50%;background:var(--blue)}
.about-title{left:402px;top:672px;font-size:27px;font-weight:700;color:var(--ink)}
.about-title b{color:var(--blue)}
.about-copy{left:402px;top:720px;width:700px;font-size:14.5px;line-height:21px;color:var(--grey)}
.about-copy p+p{margin-top:17px}
.btn{display:inline-block;font-weight:700;font-size:16px;text-transform:uppercase;padding:9px 14px;border-radius:3px;color:var(--white);background:var(--blue)}
.about-btn{left:402px;top:975px}

/* services */
.services{left:0;top:1082px;width:1200px;height:470px;background:var(--blue);color:var(--white)}
.section-title{width:1200px;text-align:center;font-size:27px;font-weight:700}
.services .section-title{top:40px;left:0}
.services-intro{left:0;top:88px;width:1200px;text-align:center;font-size:15.5px;font-weight:600;line-height:24px}
.service{display:flex;gap:14px;width:330px}
.service-icon{width:92px;height:92px;flex:none;border:2px solid var(--white);background:#1276c6;display:flex;align-items:center;justify-content:center}
.service h3{font-size:17px;font-weight:600;color:var(--sky);line-height:20px}
.service p{font-size:13px;line-height:17px;color:var(--white)}

/* map */
.map-title{left:0;top:1588px;width:1200px;text-align:center;font-size:27px;font-weight:700;color:var(--ink)}
.map-title b{color:var(--blue)}
.world-map{left:50px;top:1640px;width:820px;height:460px;border-radius:30px;background:radial-gradient(ellipse at 45% 40%,#7fdcf3 0%,#2a86cf 45%,#cfe3f3 80%,#fff 100%)}
.countries{top:1670px;font-size:14px;font-weight:600;line-height:19.6px;color:var(--ink);list-style:none}
.map-btn{left:522px;top:2100px;padding:10px 28px}

/* join */
.join{left:0;top:2205px;width:1200px;height:233px;background:var(--blue);color:var(--white)}
.join .section-title{left:0;top:42px}
.join-copy{left:0;top:86px;width:1200px;text-align:center;font-size:15.5px}
.join-copy span{color:var(--sky)}
.join-btn{left:520px;top:130px;background:transparent;border:2px solid var(--white)}

/* contact */
.contact-brand{left:55px;top:2528px;font-size:52px;font-weight:700;color:var(--blue);line-height:1}
.contact-list{left:268px;top:2480px;font-size:15.5px;font-weight:600;line-height:22px;list-style:none}
.contact-list li{display:flex;gap:14px;margin-bottom:16px}
.contact-list svg{flex:none;margin-top:3px}
.field{background:var(--field);font-size:13px;color:#666;padding:9px 16px;border:none;font-family:inherit}
.send{left:846px;top:2586px;width:104px;height:38px;background:#111;color:var(--white);font-weight:700;font-size:14px;display:flex;align-items:center;justify-content:center}
.footer{left:0;top:2672px;width:1200px;height:39px;background:var(--blue);color:var(--white);font-size:10px;font-weight:700;text-align:center;padding-top:5px;text-transform:uppercase}
</style>
</head>
<body>

<header class="hero abs">
  <div class="hero-photo" role="img" aria-label="Photograph of business people walking across a paved square, long shadows in low sunlight"></div>
  <div class="brand abs">Varnek</div>
  <div class="social abs"><span></span><span></span><span></span></div>
  <nav class="nav abs">
    <a class="active">Home</a><a>About us</a><a>Our services</a><a>Our expertise</a><a>Our clients</a><a>Join our team</a><a>Contact</a>
  </nav>
  <div class="slider-dots abs"><span class="on"></span><span></span><span></span><span></span></div>
  <p class="hero-caption abs">We enable organizations to achieve success in complex, hostile and volatile environments by providing dynamic tailored solutions delivered by people who are not only experts in their field, but who are culturally sensitive, politically aware and aligned to the values, drivers and objectives of your organisation. We are not a large corporation, nor do we want to be. Remaining flexible and focused on those who trust us with their most precious assets is our critical path.</p>
</header>

<section class="about">
  <div class="about-mark abs"></div>
  <h2 class="about-title abs">ABOUT <b>VARNEK</b></h2>
  <div class="about-copy abs">
    <p>Lorem ipsum dolor sit amet, consectetuer adipiscing elit, sed diam nonummy nibh euis mod tincidunt ut laoreet dolore magna aliquam erat volutpat. Ut wisi enim adminim veniam, quis nostrud exerci tatio ullamcorper suscipit lobortis nisl ut aliquip exea commodo consequat. Duis autem vel eum iriure dolor in hendrerit in vulputate velit esse moles tie consequat, vel illum dolore eu feugia nulla facilisis at veroe ros et accumsan et.</p>
    <p>Typi non habent claritatem insitam; est usus legentis in iis qui facit eorum claritatem. Investigationes demonstraverunt lectores legere me lius quod ii legunt saepius. Claritas es etiam processus dynamicus, qui sequitur mutationem consuetudium lectorum. Mirumest notare quam littera gothica, quam nunc putamus parum claram, anteposuerit littera rum formas humanitatis per seacula quarta decima et quin ta decima.</p>
  </div>
  <span class="btn about-btn abs">Discover more</span>
</section>

<div class="divider abs" style="top:1056px"></div>

<section class="services abs">
  <h2 class="section-title abs">OUR SERVICES</h2>
  <p class="services-intro abs">Varnek International Services (www.varnekis-example.com) provides security services of various types in challenging<br>or high threat environments internationally for government and private sector organizations.</p>

  <div class="service abs" style="left:100px;top:183px">
    <div class="service-icon"><svg width="60" height="60" viewBox="0 0 60 60" fill="none" stroke="#fff" stroke-width="4"><circle cx="30" cy="30" r="17"/><path d="M10 16a26 26 0 0 0 0 28M50 16a26 26 0 0 1 0 28"/><path d="M30 20v12"/><circle cx="30" cy="39" r="1.5" fill="#fff"/></svg></div>
    <div><h3>Risk Assessment</h3><p>Lorem ipsum dolor sit amet, consec tetuer adipiscing elit, sed diam no nummy nibh euismod tincidunt ut laoreet dolore magna.</p></div>
  </div>
  <div class="service abs" style="left:452px;top:183px">
    <div class="service-icon"><svg width="60" height="60" viewBox="0 0 60 60" fill="none" stroke="#fff" stroke-width="3.5"><rect x="14" y="10" width="32" height="42" rx="2"/><rect x="23" y="6" width="14" height="8" fill="#fff"/><path d="M19 24l3 3 5-5M19 34l3 3 5-5M19 44l3 3 5-5M31 25h10M31 35h10M31 45h10"/></svg></div>
    <div><h3>Security Audits &amp; Training</h3><p>Lorem ipsum dolor sit amet, consec tetuer adipiscing elit, sed diam no nummy nibh euismod tincidunt ut laoreet dolore magna.</p></div>
  </div>
  <div class="service abs" style="left:805px;top:183px">
    <div class="service-icon"><svg width="60" height="60" viewBox="0 0 60 60"><rect x="8" y="18" width="44" height="32" rx="3" fill="#fff"/><path d="M22 18v-6h16v6" fill="none" stroke="#fff" stroke-width="4"/><path d="M26 26h8v6h6v8h-6v6h-8v-6h-6v-8h6z" fill="#1276c6"/></svg></div>
    <div><h3>Medical Support</h3><p>Lorem ipsum dolor sit amet, consec tetuer adipiscing elit, sed diam no nummy nibh euismod tincidunt ut laoreet dolore magna.</p></div>
  </div>
  <div class="service abs" style="left:100px;top:320px">
    <div class="service-icon"><svg width="60" height="60" viewBox="0 0 60 60" fill="none" stroke="#fff" stroke-width="4"><path d="M30 8l18 7v14c0 12-8 19-18 23-10-4-18-11-18-23V15z"/><path d="M24 20l12 22M30 17l10 18" stroke-width="3"/></svg></div>
    <div><h3>Close Protection</h3><p>Lorem ipsum dolor sit amet, consec tetuer adipiscing elit, sed diam no nummy nibh euismod tincidunt ut laoreet dolore magna.</p></div>
  </div>
  <div class="service abs" style="left:452px;top:320px">
    <div class="service-icon"><svg width="60" height="60" viewBox="0 0 60 60"><path d="M8 14h14l14 18 4-4 4 20-20-4 4-4-12-16H8z" fill="#fff"/></svg></div>
    <div><h3>Crisis Management</h3><p>Lorem ipsum dolor sit amet, consec tetuer adipiscing elit, sed diam no nummy nibh euismod tincidunt ut laoreet dolore magna.</p></div>
  </div>
  <div class="service abs" style="left:805px;top:320px">
    <div class="service-icon"><svg width="60" height="60" viewBox="0 0 60 60" fill="none" stroke="#fff" stroke-width="4"><rect x="28" y="10" width="20" height="40"/><path d="M8 30h28M26 22l10 8-10 8"/></svg></div>
    <div><h3>Evacuation Coordination</h3><p>Lorem ipsum dolor sit amet, consec tetuer adipiscing elit, sed diam no nummy nibh euismod tincidunt ut laoreet dolore magna.</p></div>
  </div>
</section>

<div class="divider abs" style="top:1526px"></div>

<section class="map">
  <h2 class="map-title abs">VARNEK ASSOCIATES HAVE EXPERIENCE IN <b>OVER 21 COUNTRIES</b></h2>
  <div class="world-map abs" role="img" aria-label="Dotted world map in blue with the countries of operation highlighted in light cyan"></div>
  <ul class="countries abs" style="left:878px">
    <li>Afghanistan</li><li>Austria</li><li>Bosnia</li><li>Canada</li><li>Central African Republic</li><li>Egypt</li><li>France</li><li>Iraq</li><li>Libya</li><li>Mali</li><li>Nigeria</li>
  </ul>
  <ul class="countries abs" style="left:1077px">
    <li>Qatar</li><li>Rwanda</li><li>Somalia</li><li>Somaliland</li><li>Sudan</li><li>Tunisia</li><li>Turkey</li><li>UAE</li><li>UK</li><li>USA</li><li>Yemen</li>
  </ul>
  <span class="btn map-btn abs">Learn more</span>
</section>

<div class="divider abs" style="top:2179px"></div>

<section class="join abs">
  <h2 class="section-title abs">JOIN OUR TEAM</h2>
  <p class="join-copy abs">For more information or to join the Varnek IS team of experienced specialists, contact us at <span>info@varnekis-example.com</span> or <span>hr@varnekis-example.com</span></p>
  <span class="btn join-btn abs">Discover more</span>
</section>

<div class="divider abs" style="top:2412px"></div>

<section class="contact">
  <div class="contact-brand abs">Varnek</div>
  <ul class="contact-list abs">
    <li><svg width="14" height="18" viewBox="0 0 14 18"><path d="M7 0a7 7 0 0 1 7 7c0 5-7 11-7 11S0 12 0 7a7 7 0 0 1 7-7z" fill="#0a5fa8"/><circle cx="7" cy="7" r="2.6" fill="#fff"/></svg><span>Harbour House<br>12 Example Street<br>Edinburgh | UK | EH1 0ZZ</span></li>
    <li style="margin-top:16px"><svg width="18" height="16" viewBox="0 0 18 16"><path d="M2 3c3-3 11-3 14 0l-2 3-3-1V3H7v2L4 6z M3 8h12l2 7H1z" fill="#0a5fa8"/></svg><span>+ 44 (0)800 555 0142</span></li>
    <li><svg width="18" height="14" viewBox="0 0 18 14"><rect width="18" height="14" fill="#0a5fa8"/><path d="M1 1l8 7 8-7" fill="none" stroke="#fff" stroke-width="1.6"/></svg><span>info@varnekis-example.com</span></li>
  </ul>
  <div class="field abs" style="left:540px;top:2492px;width:300px;height:38px">Name</div>
  <div class="field abs" style="left:540px;top:2540px;width:300px;height:38px">Email</div>
  <div class="field abs" style="left:540px;top:2588px;width:300px;height:38px">Phone</div>
  <div class="field abs" style="left:846px;top:2492px;width:312px;height:86px">Message</div>
  <div class="send abs">SEND</div>
</section>

<footer class="footer abs">Copyright © 2015 Varnek. All rights reserved.</footer>

</body>
</html>
```